Business Card Design

It is an assisted living facility. I wanted the name to reflect that we are a step above other facilities; i.e., professionally decorated rooms, cloth napkins, family dinners, etc. My motto is: COME WHERE YOU ARE CELEBRATED! Also, I have thought about having a house held with the "Hands" and the motto around it but I have seen that logo used other places. In other words, HELP!

I do not have a photo yet, but the photographer is coming next week. I would like the back of the card to have a picture of the facility.

Industry/Entity Type

Business

Contact Information for Business Card

BRIGHT MEADOW ASSISTED LIVING, LLC, 2938 Quillmont Dr., FL 33482-7261
Phone: (555) 214-6037; Fax: (555)
Linda Pruett, Owner/Administrator

```html
<!DOCTYPE html>
<html lang="en">
<head>
<meta charset="utf-8">
<title>Bright Meadow Assisted Living – Business Cards</title>
<link href="https://fonts.googleapis.com/css2?family=Anton&family=Francois+One&family=Arimo:wght@400;700&display=swap" rel="stylesheet">
<style>
  :root {
    --page-bg: #efece7;
    --charcoal: #2b2b2b;
    --leaf: #5aad0f;
    --leaf-light: #a6d63a;
    --brand-green: #1f9a10;
    --deep-green: #119200;
    --orange: #f59c0f;
    --ink: #2a2a2a;
    --white: #ffffff;
  }
  * { margin: 0; padding: 0; box-sizing: border-box; }
  html, body { width: 839px; height: 1200px; overflow: hidden; }
  body { background: var(--page-bg); position: relative; font-family: "Arimo", Arial, sans-serif; }

  .card {
    position: absolute;
    width: 662px;
    height: 398px;
    overflow: hidden;
    box-shadow: 0 2px 6px rgba(0,0,0,.25);
  }
  .card--dark { left: 88px; top: 80px; }
  .card--light { left: 88px; top: 708px; }

  .card__backdrop { position: absolute; inset: 0; width: 100%; height: 100%; }

  .motto {
    position: absolute;
    left: 0; right: 0;
    text-align: center;
    font-family: "Anton", Impact, sans-serif;
    font-size: 31px;
    letter-spacing: .5px;
    color: var(--white);
    -webkit-text-stroke: 1.4px #111;
    paint-order: stroke fill;
    text-shadow: 1px 2px 0 #111;
    line-height: 1;
  }
  .card--dark .motto { top: 30px; }
  .card--light .motto { top: 325px; }

  .brand-name {
    position: absolute;
    font-family: "Francois One", "Arial Narrow", sans-serif;
    font-weight: 400;
    font-size: 27px;
    line-height: 1.2;
    text-align: center;
    width: 230px;
  }
  .card--dark .brand-name { left: 28px; top: 235px; color: var(--leaf-light); }
  .card--light .brand-name { left: 22px; top: 220px; color: var(--brand-green); }

  .contact {
    position: absolute;
    text-align: right;
    color: var(--white);
  }
  .card--dark .contact { right: 75px; top: 155px; }
  .card--light .contact { right: 90px; top: 102px; color: var(--ink); }

  .contact__name { font-weight: 700; font-size: 22px; line-height: 26px; }
  .contact__title { font-size: 19px; line-height: 24px; margin-bottom: 20px; }
  .contact__row {
    display: flex; justify-content: flex-end; align-items: center; gap: 4px;
    font-size: 17px; line-height: 20px; height: 20px; margin-bottom: 16px;
  }
  .icon { width: 20px; height: 20px; flex: none; }
  .icon path, .icon rect { fill: var(--orange); }
</style>
</head>
<body>

<!-- Front, dark version -->
<section class="card card--dark">
  <svg class="card__backdrop" viewBox="0 0 662 398" aria-hidden="true">
    <rect width="662" height="398" fill="#56ae0c"/>
    <path d="M0,185 C8,118 60,84 170,82 L662,82 L662,92 L170,92 C70,94 14,125 0,195 Z" fill="#b9e05a"/>
    <path d="M0,195 C14,125 70,94 170,92 L662,92 L662,398 L0,398 Z" fill="var(--charcoal)"/>
  </svg>
  <h2 class="motto">COME WHERE YOU ARE CELEBRATED!</h2>
  <p class="brand-name">BRIGHT MEADOW<br>ASSISTED LIVING</p>
  <div class="contact">
    <p class="contact__name">Linda Pruett</p>
    <p class="contact__title">Owner/Administrator</p>
    <p class="contact__row">
      <svg class="icon" viewBox="0 0 20 20" aria-hidden="true"><path d="M4 1 L8 1 L9 6 L6.5 7.5 C7.5 11 9 13 12 14.5 L13.5 12 L18.5 13 L18.5 17 C18.5 18 17.5 19 16 19 C8 18 2 12 1 4 C1 2.5 2.5 1 4 1 Z"/></svg>
      (555) 214-6037
    </p>
    <p class="contact__row">
      <svg class="icon" viewBox="0 0 20 20" aria-hidden="true"><rect x="5" y="1" width="10" height="6"/><path d="M2 8 H18 V15 H15 V12 H5 V15 H2 Z"/><rect x="6" y="13" width="8" height="6"/></svg>
      (555)
    </p>
    <p class="contact__row">
      <svg class="icon" viewBox="0 0 20 20" aria-hidden="true"><path d="M10 1 C5.5 1 3 4 3 7.5 C3 12 10 19 10 19 C10 19 17 12 17 7.5 C17 4 14.5 1 10 1 Z M10 5 A2.6 2.6 0 1 0 10.01 5 Z"/></svg>
      2938 Quillmont Dr., FL 33482-7261
    </p>
  </div>
</section>

<!-- Front, light version -->
<section class="card card--light">
  <svg class="card__backdrop" viewBox="0 0 662 398" aria-hidden="true">
    <rect width="662" height="398" fill="var(--deep-green)"/>
    <path d="M0,0 H662 V34 H150 C80,34 25,52 0,95 Z" fill="var(--orange)"/>
    <path d="M0,150 C6,82 52,48 130,47 L662,47 L662,212 C652,278 620,305 560,307 L0,307 Z" fill="var(--white)"/>
  </svg>
  <p class="brand-name">BRIGHT MEADOW<br>ASSISTED LIVING</p>
  <div class="contact">
    <p class="contact__name">Linda Pruett</p>
    <p class="contact__title">Owner/Administrator</p>
    <p class="contact__row">
      <svg class="icon" viewBox="0 0 20 20" aria-hidden="true"><path d="M4 1 L8 1 L9 6 L6.5 7.5 C7.5 11 9 13 12 14.5 L13.5 12 L18.5 13 L18.5 17 C18.5 18 17.5 19 16 19 C8 18 2 12 1 4 C1 2.5 2.5 1 4 1 Z"/></svg>
      (555) 214-6037
    </p>
    <p class="contact__row">
      <svg class="icon" viewBox="0 0 20 20" aria-hidden="true"><rect x="5" y="1" width="10" height="6"/><path d="M2 8 H18 V15 H15 V12 H5 V15 H2 Z"/><rect x="6" y="13" width="8" height="6"/></svg>
      (555)
    </p>
    <p class="contact__row">
      <svg class="icon" viewBox="0 0 20 20" aria-hidden="true"><path d="M10 1 C5.5 1 3 4 3 7.5 C3 12 10 19 10 19 C10 19 17 12 17 7.5 C17 4 14.5 1 10 1 Z M10 5 A2.6 2.6 0 1 0 10.01 5 Z"/></svg>
      2938 Quillmont Dr., FL 33482-7261
    </p>
  </div>
  <h2 class="motto">COME WHERE YOU ARE CELEBRATED!</h2>
</section>

</body>
</html>
```